Breezeway Comfort business cards design

Need a business card design for a Heating and Air Conditioning business. I need these items included.
Business name: Breezeway Comfort
Owner: Marcus Tollefsen
License # 2874590
Phone number # 555-382-4071
Email: breezewaycomfortair@mailvista.example
Sales
Service
Installation
Maintenance

Heating and Air Conditioning

Requirements
Must have
• Company name , license number , phone number , email

```html
<!DOCTYPE html>
<html lang="en">
<head>
<meta charset="utf-8">
<title>Breezeway Comfort – Business Cards</title>
<link rel="stylesheet" href="https://fonts.googleapis.com/css2?family=Lato:wght@400;700;900&display=swap">
<style>
  :root {
    --brand-blue: #1e4a9c;
    --brand-orange: #ee6446;
    --ink: #111111;
    --card-white: #ffffff;
    --backdrop: #e9ebea;
    --card-shadow: 0 4px 8px rgba(0,0,0,0.35);
  }
  * { box-sizing: border-box; margin: 0; padding: 0; }
  html, body {
    width: 1200px; height: 1200px; overflow: hidden;
    background: var(--backdrop);
    font-family: "Lato", Arial, sans-serif;
  }
  .sheet { position: relative; width: 1200px; height: 1200px; }
  .card {
    position: absolute; left: 209px; width: 783px; height: 447px;
    box-shadow: var(--card-shadow); overflow: hidden;
  }
  .card-front { top: 122px; background: var(--card-white); }
  .card-back { top: 630px; background: var(--brand-blue); }

  /* front: brand block */
  .brand-block {
    position: absolute; left: 50px; top: 100px; width: 304px;
    display: flex; flex-direction: column; align-items: center;
  }
  .brand-dot {
    width: 84px; height: 84px; border-radius: 50%;
    background: var(--brand-orange); margin-bottom: 22px;
  }
  .brand-name {
    font-weight: 900; font-size: 44px; line-height: 1.02;
    color: var(--brand-blue); text-align: center; letter-spacing: 1px;
  }

  /* front: owner */
  .owner-row {
    position: absolute; left: 389px; right: 0; top: 99px;
    display: flex; align-items: center; gap: 16px;
  }
  .owner-name {
    flex: none;
    font-weight: 700; font-size: 29px; letter-spacing: 1.5px; line-height: 36px;
    color: var(--brand-blue); text-transform: uppercase;
  }
  .owner-rule {
    flex: 1; min-width: 30px; height: 22px;
    background: var(--brand-blue);
  }
  .owner-title {
    position: absolute; left: 390px; top: 132px;
    font-weight: 700; font-size: 25px; color: var(--ink);
  }

  /* front: contact */
  .contact {
    position: absolute; left: 391px; top: 244px; height: 85px;
    border-left: 1.5px solid var(--brand-blue); padding-left: 13px;
    color: var(--ink);
  }
  .contact-line {
    display: flex; align-items: center; gap: 8px;
    font-weight: 700; font-size: 18px; height: 25px; white-space: nowrap;
  }
  .contact-line svg { width: 18px; height: 16px; flex: none; fill: var(--brand-blue); }
  .contact-line .icon-gap { width: 2px; }
  .services {
    display: flex; font-size: 13.6px; font-weight: 400; margin-top: 2px; color: var(--ink);
  }
  .services span { padding: 0 7px; border-left: 1px solid #555; line-height: 16px; }
  .services span:first-child { padding-left: 1px; border-left: none; }

  /* front: bottom bands */
  .band { position: absolute; bottom: 0; height: 28px; }
  .band-blue { left: 0; width: 382px; background: var(--brand-blue); }
  .band-orange { left: 400px; width: 383px; background: var(--brand-orange); }

  /* back */
  .back-brand {
    position: absolute; inset: 0;
    display: flex; align-items: center; justify-content: center; gap: 40px;
  }
  .back-dot { width: 150px; height: 150px; border-radius: 50%; background: var(--card-white); }
  .back-name {
    font-weight: 900; font-size: 60px; line-height: 1.02;
    color: var(--card-white); letter-spacing: 1.5px;
  }
</style>
</head>
<body>
<main class="sheet">
  <section class="card card-front">
    <div class="brand-block">
      <div class="brand-dot"></div>
      <div class="brand-name">Breezeway<br>Comfort</div>
    </div>

    <div class="owner-row">
      <h1 class="owner-name">Marcus Tollefsen</h1>
      <div class="owner-rule"></div>
    </div>
    <p class="owner-title">Owner</p>

    <div class="contact">
      <p class="contact-line">License # 2874590</p>
      <p class="contact-line">
        <span class="icon-gap"></span>
        <svg viewBox="0 0 24 24" aria-hidden="true"><path d="M6.6 10.8a15.1 15.1 0 0 0 6.6 6.6l2.2-2.2c.3-.3.7-.4 1-.2 1.1.4 2.3.6 3.6.6.6 0 1 .4 1 1V20c0 .6-.4 1-1 1C10.6 21 3 13.4 3 4c0-.6.4-1 1-1h3.5c.6 0 1 .4 1 1 0 1.3.2 2.5.6 3.6.1.3 0 .7-.2 1z"/></svg>
        555-382-4071
      </p>
      <p class="contact-line">
        <svg viewBox="0 0 24 18" aria-hidden="true"><path d="M0 0h24v18H0z M2 2v1l10 7 10-7V2z M2 5.5V16h20V5.5l-10 7z" fill-rule="evenodd"/></svg>
        breezewaycomfortair@mailvista.example
      </p>
      <p class="services">
        <span>SALES</span><span>SERVICE</span><span>INSTALLATION</span><span>MAINTENANCE</span>
      </p>
    </div>

    <div class="band band-blue"></div>
    <div class="band band-orange"></div>
  </section>

  <section class="card card-back">
    <div class="back-brand">
      <div class="back-dot"></div>
      <div class="back-name">Breezeway<br>Comfort</div>
    </div>
  </section>
</main>
</body>
</html>
```